Business Card Design

We need a business card designed to the point of print ready to take to our printers. the design should be professional, easy to read and simple. The cards should represent our business as professional and trust worthy.

Attached are several versions o the logo, and also the details for the card to be printed. please do communicate if different versions of the logo is required.

Business

```html
<!DOCTYPE html>
<html lang="en">
<head>
<meta charset="utf-8">
<title>TallyBack Business Cards</title>
<link rel="stylesheet" href="https://fonts.googleapis.com/css2?family=Exo+2:ital,wght@0,500;0,600;1,400;1,500&display=swap">
<style>
  :root {
    --backdrop: #b3b1b2;
    --frame-grey: #666465;
    --text-grey: #58585a;
    --accent: #f39a1e;
    --paper: #ffffff;
  }
  * { box-sizing: border-box; margin: 0; padding: 0; }
  html, body { width: 1200px; height: 848px; overflow: hidden; }
  body {
    background: var(--backdrop);
    font-family: "Exo 2", sans-serif;
    position: relative;
  }
  .card {
    position: absolute;
    width: 465px;
    height: 284px;
    padding: 16px;
  }
  .card--front { background: var(--frame-grey); }
  .card--back { background: var(--paper); }
  .row-1 { top: 99px; }
  .row-2 { top: 464px; }
  .col-front { left: 87px; }
  .col-back { left: 648px; }

  .face {
    position: relative;
    width: 100%;
    height: 100%;
    background: var(--paper);
    text-align: center;
  }
  .wordmark {
    position: absolute;
    top: 20px;
    left: 0; right: 0;
    font-weight: 600;
    font-size: 27px;
    color: var(--frame-grey);
    letter-spacing: 0.2px;
  }
  .identity {
    position: absolute;
    top: 113px;
    left: 0; right: 0;
    font-style: italic;
    font-size: 19px;
  }
  .identity .person { color: var(--accent); }
  .identity .role { color: var(--text-grey); font-size: 17px; }
  .contact {
    position: absolute;
    top: 186px;
    left: 0; right: 0;
    list-style: none;
    font-style: italic;
    font-size: 13px;
    line-height: 17.5px;
    color: var(--text-grey);
  }
  .back-field {
    position: relative;
    width: 100%;
    height: 100%;
    background: linear-gradient(135deg, #6c6a6b, #5f5d5e);
    display: flex;
    align-items: center;
    justify-content: center;
  }
  .web {
    position: relative;
    font-style: italic;
    font-weight: 500;
    font-size: 15px;
    color: var(--accent);
    top: -16px;
  }
</style>
</head>
<body>

  <section class="card card--front row-1 col-front">
    <div class="face">
      <div class="wordmark">TallyBack Pty Ltd</div>
      <p class="identity"><span class="person">Renata Vossel /</span> <span class="role">Managing Director</span></p>
      <ul class="contact">
        <li>+61 400 555 101</li>
        <li>rvossel@tallyback.com.au</li>
        <li>PO Box 1180 Harbourside Qld 4999</li>
      </ul>
    </div>
  </section>

  <section class="card card--back row-1 col-back">
    <div class="back-field" role="img" aria-label="Repeating pattern of dollar signs in grey tones">
      <span class="web">www.tallyback.com.au</span>
    </div>
  </section>

  <section class="card card--front row-2 col-front">
    <div class="face">
      <div class="wordmark">TallyBack Pty Ltd</div>
      <p class="identity"><span class="person">Liam Dorrance /</span> <span class="role">Director</span></p>
      <ul class="contact">
        <li>+61 400 555 202</li>
        <li>ldorrance@tallyback.com.au</li>
        <li>PO Box 1180 Harbourside Qld 4999</li>
      </ul>
    </div>
  </section>

  <section class="card card--back row-2 col-back">
    <div class="back-field" role="img" aria-label="Repeating pattern of dollar signs in grey tones">
      <span class="web">www.tallyback.com.au</span>
    </div>
  </section>

</body>
</html>
```